Business Card Design Project

we need a business card design for our company: www.plomvik.ch
It's important to include our already existing logo (see website)

```html
<!DOCTYPE html>
<html lang="de">
<head>
<meta charset="utf-8">
<title>Plomvik – Visitenkarte</title>
<link rel="stylesheet" href="https://fonts.googleapis.com/css2?family=Open+Sans:ital,wght@0,400;0,600;0,700;1,400&display=swap">
<style>
  :root {
    --backdrop: #ececec;
    --brand-blue: #0a76c4;
    --brand-blue-light: #3b8fd8;
    --title-blue: #6aa7dc;
    --card-white: #ffffff;
    --text-grey: #4a4a4a;
    --card-shadow: rgba(0, 0, 0, 0.18);
  }
  * { box-sizing: border-box; margin: 0; padding: 0; }
  html, body {
    width: 1200px;
    height: 900px;
    overflow: hidden;
    background: var(--backdrop);
    font-family: "Open Sans", Arial, sans-serif;
  }
  .canvas {
    width: 1200px;
    height: 900px;
    display: flex;
    align-items: center;
    justify-content: center;
    gap: 60px;
  }
  .card {
    width: 510px;
    height: 320px;
    border-radius: 22px;
    box-shadow: 0 6px 18px var(--card-shadow);
    position: relative;
    overflow: hidden;
  }

  /* Front side */
  .card--front {
    background: var(--brand-blue);
    color: var(--card-white);
  }
  .front-lockup {
    position: absolute;
    left: 0;
    top: 86px;
    padding-left: 26px;
  }
  .wordmark {
    font-weight: 700;
    font-size: 76px;
    line-height: 1;
    letter-spacing: -1px;
    white-space: nowrap;
  }
  .card--front .wordmark { color: var(--card-white); }
  .tagline {
    margin-top: 14px;
    margin-left: 62px;
    font-weight: 700;
    font-size: 15px;
    letter-spacing: 0.2px;
    white-space: nowrap;
  }
  .front-web {
    margin-left: 62px;
    margin-top: 2px;
    font-weight: 700;
    font-size: 15px;
  }

  /* Back side */
  .card--back {
    background: var(--card-white);
  }
  .back-wordmark {
    position: absolute;
    left: 22px;
    top: 148px;
    font-size: 44px;
    color: var(--brand-blue-light);
  }
  .contact {
    position: absolute;
    left: 270px;
    top: 54px;
    color: var(--text-grey);
    font-size: 14px;
    line-height: 1.4;
  }
  .contact__name {
    color: var(--brand-blue);
    font-weight: 700;
    font-size: 19px;
    line-height: 1.2;
  }
  .contact__title {
    color: var(--title-blue);
    font-style: italic;
    font-size: 14px;
  }
  .contact__company {
    margin-top: 16px;
    color: var(--brand-blue);
    font-weight: 700;
    font-size: 15px;
  }
  .contact__lines {
    margin-top: 22px;
    font-size: 12px;
  }
  .contact__row {
    display: flex;
    align-items: center;
    gap: 10px;
    margin-bottom: 6px;
  }
  .contact__icon {
    width: 16px;
    height: 14px;
    flex: none;
  }
</style>
</head>
<body>
<main class="canvas">

  <section class="card card--front" aria-label="Vorderseite">
    <div class="front-lockup">
      <div class="wordmark">Plomvik</div>
      <p class="tagline">BUSINESS SOFTWARE SOLUTIONS</p>
      <p class="front-web">www.plomvik.ch</p>
    </div>
  </section>

  <section class="card card--back" aria-label="Rückseite">
    <div class="wordmark back-wordmark">Plomvik</div>

    <div class="contact">
      <p class="contact__name">Name</p>
      <p class="contact__title">Title</p>

      <p class="contact__company">Plomvik AG</p>
      <p>Lindenweg 12</p>
      <p>8005 Zürich</p>

      <div class="contact__lines">
        <p class="contact__row">
          <svg class="contact__icon" viewBox="0 0 16 14" aria-hidden="true">
            <path d="M1 5 Q8 0 15 5 L13 7 L11 5.5 L5 5.5 L3 7 Z" fill="var(--brand-blue)"/>
            <rect x="3" y="7" width="10" height="6" rx="1" fill="var(--brand-blue)"/>
            <circle cx="8" cy="10" r="1.6" fill="var(--card-white)"/>
          </svg>
          <span>+41 44 512 34 56</span>
        </p>
        <p class="contact__row">
          <svg class="contact__icon" viewBox="0 0 16 14" aria-hidden="true">
            <rect x="1" y="2" width="14" height="10" fill="none" stroke="var(--brand-blue)" stroke-width="1.5"/>
            <path d="M1 2 L8 8 L15 2" fill="none" stroke="var(--brand-blue)" stroke-width="1.5"/>
          </svg>
          <span>emailaddress@plomvik.ch</span>
        </p>
      </div>
    </div>
  </section>

</main>
</body>
</html>
```